PPT template for boutique strategic planning, accounting and taxation firm

We are a boutique firm that provides strategic, accounting and tax advice to our clients. The work we are doing is increasingly strategic work and we are required to produce reports and presentations and our current templates are simply not sufficient.
As you can see from the examples attached, we have very limited skills in house re design! We have attached a PPT document and word document (that should be PPT) that we use regularly as examples of the content. Excel worksheets are regularly embedded into the presentation (in both blue and orange - see below re colours)
Not specific to one area but typically these clients are famous for their own brand and are creating value in their industry through creating their own brand and we want to produce documents of a similar standard.
A Powerpoint Document Slide Template
Cover page layout, back page, intermediate page heading, in colours and styles based on the logo, title styles, and an intermediate or chapter heading slide style. Many of our presentations contain slides with tables, diagrams, flowcharts and text, including simple lists of bullet points. As above, you will see in our style guide that we have three coloured logos – we would like one version in blue and one version in orange please. Again, the cover should be bold and draw attention but remain professional.
We are looking for something that works in both 4:3 and 16:9 (or two templates please)
We like a clear professional and simple look.
Deliverable: PowerPoint template file (.potx extension) for PowerPoint 2007 with at least a “cover” layout, a “title and content” layout, and a simplified slide layout, as well as “back cover”. Please embed any fonts used.
Target Market(s)
Many of our clients are retail clients or have strong brands of their own.
Industry/Entity Type
Accounting
Requirements
Must have
- Harrowby & Co logo on each page.
Must have a cover page (please be bold but professional)
A selection of "standard" slides - dot points, detailed written content, example diagrams, flow charts etc.
A back cover
Nice to have
- We would like to have a copy done in both the blue and orange versions attached. Happy for the winner to complete the other colour after the winner is selected.
Prefer Arial logo but open to suggestions. Must be easy to read and professional
Should not have
- Nothing cartoonish

```html
<!DOCTYPE html>
<html lang="en">
<head>
<meta charset="utf-8">
<title>Harrowby &amp; Co – Slide Template</title>
<link rel="stylesheet" href="https://fonts.googleapis.com/css2?family=Open+Sans:wght@300;400;600;700&display=swap">
<style>
  :root{
    --stage:#6e6e6e;
    --paper:#ffffff;
    --navy:#0f5ea9;
    --blue:#1a6fba;
    --mid-blue:#2f86cf;
    --sky:#1f9bef;
    --teal:#4fc2c4;
    --orange:#f39035;
    --orange-deep:#ee7b22;
    --slate:#43484e;
    --ink:#3c3f44;
    --grey-text:#5a5e63;
    --rule:#d9d9d9;
    --diagram-box:#5b9bd5;
    --amber:#ffc000;
  }
  *{box-sizing:border-box;margin:0;padding:0}
  html,body{width:1200px;height:960px;overflow:hidden;background:var(--stage)}
  body{position:relative;font-family:"Open Sans",Arial,sans-serif;color:var(--ink)}

  .slide{position:absolute;width:576px;height:432px;background:var(--paper);overflow:hidden}
  .slide--cover{left:16px;top:34px}
  .slide--method{left:610px;top:34px}
  .slide--values{left:16px;top:490px}
  .slide--growth{left:610px;top:490px}

  /* cover */
  .cover-bands{position:absolute;left:0;top:0;height:100%;display:flex}
  .cover-bands span{display:block;height:100%}
  .band-navy{width:94px;background:var(--navy)}
  .band-blue{width:12px;background:var(--mid-blue)}
  .band-teal{width:55px;background:var(--teal)}
  .band-orange{width:14px;background:var(--orange)}
  .cover-title{position:absolute;left:196px;top:81px;font-size:27px;font-weight:700;font-variant:small-caps;color:var(--navy);letter-spacing:.3px;white-space:nowrap}
  .cover-presenter{position:absolute;left:196px;top:128px;font-size:14px;font-weight:700;color:var(--grey-text)}
  .cover-date{position:absolute;left:196px;top:167px;font-size:10px;color:var(--grey-text)}
  .brand-name{position:absolute;left:195px;top:343px;font-size:31px;font-weight:600;color:#50555b;line-height:1;white-space:nowrap}
  .brand-tagline{position:absolute;left:196px;top:381px;font-size:8.5px;font-weight:700;color:#50555b;white-space:nowrap}

  /* content slide frame */
  .side-bands{position:absolute;right:0;top:0;height:380px;width:55px}
  .side-bands .light{position:absolute;left:0;top:0;width:14px;height:100%;background:var(--mid-blue)}
  .side-bands .dark{position:absolute;left:17px;top:0;right:0;height:100%;background:var(--navy)}
  .brand-mark{position:absolute;right:12px;bottom:5px}
  .brand-mark .dot{display:block;width:40px;height:40px;border-radius:50%;background:var(--navy)}
  .slide-heading{position:absolute;left:20px;top:16px;font-size:19px;font-weight:400;color:var(--blue);white-space:nowrap}
  .heading-rule{position:absolute;left:20px;top:49px;width:493px;height:1.5px;background:var(--orange)}
  .page-no{position:absolute;left:14px;bottom:14px;font-size:8px;color:var(--ink)}

  /* method slide */
  .subheading{position:absolute;left:20px;top:58px;font-size:14px;font-weight:400;color:var(--blue)}
  .body-copy{position:absolute;left:20px;top:82px;font-size:9.2px;line-height:20.4px;color:var(--ink);white-space:nowrap}
  .cycle{position:absolute;left:0;top:0;width:576px;height:432px}
  .cycle-box{position:absolute;font-size:8.2px;line-height:1.2;text-align:center;display:flex;align-items:center;justify-content:center;padding:3px}
  .cycle-box--scan{left:310px;top:73px;width:160px;height:65px;background:var(--diagram-box);color:#fff;font-size:9px}
  .cycle-box--now{left:318px;top:149px;width:134px;height:64px;background:#f4f4f4;border:1px solid #e2e2e2;color:#555}
  .cycle-box--how{left:254px;top:226px;width:100px;height:60px;background:#f4f4f4;border:1px solid #e2e2e2;color:#555}
  .cycle-box--where{left:404px;top:226px;width:110px;height:60px;background:#f4f4f4;border:1px solid #e2e2e2;color:#555}
  .cycle-box--next{left:312px;top:326px;width:144px;height:24px;background:var(--amber);color:#fff;font-size:9.5px}

  /* values slide */
  .value-list{position:absolute;left:27px;top:67px;list-style:none}
  .value-list li{position:relative;padding-left:16px;font-size:11px;line-height:30.7px;color:var(--ink);white-space:nowrap}
  .value-list li::before{content:"";position:absolute;left:0;top:13px;width:5px;height:5px;background:var(--blue)}
  .value-divider{position:absolute;left:290px;top:68px;width:1px;height:312px;background:var(--rule)}
  .quote-mark{position:absolute;left:300px;top:120px;font-size:58px;font-weight:700;color:var(--blue);line-height:1;font-family:Georgia,serif}
  .quote-lines{position:absolute;left:336px;top:150px;font-size:11.5px;color:var(--ink);white-space:nowrap}
  .quote-lines p{line-height:16px;margin-bottom:16px}
  .quote-lines em{font-style:normal;color:var(--blue)}

  /* growth slide */
  .matrix-axis-label{position:absolute;left:20px;top:60px;width:62px;font-size:10.5px;line-height:13.5px;color:var(--orange-deep);text-align:center}
  .matrix-line{position:absolute;background:#999}
  .matrix-line--axis{left:83px;top:56px;width:1px;height:320px}
  .matrix-line--corner{left:20px;top:57px;width:63px;height:1px;background:var(--orange)}
  .matrix-line--top{left:86px;top:107px;width:428px;height:1px}
  .matrix-col{position:absolute;top:84px;font-size:11px;color:var(--ink);text-align:center;width:213px}
  .matrix-row{position:absolute;left:3px;width:120px;height:30px;font-size:11px;line-height:14px;color:var(--blue);text-align:center;transform:rotate(-90deg);transform-origin:center}
  .quad{position:absolute;width:213px;height:128px;color:#fff;font-size:14px;line-height:1.25;text-align:center;display:flex;align-items:center;justify-content:center;padding:6px 18px}
  .quad--existing{left:86px;top:110px;background:var(--navy)}
  .quad--customer{left:301px;top:110px;background:var(--orange-deep);padding:6px 26px}
  .quad--product{left:86px;top:240px;background:var(--slate);align-items:flex-start;padding:18px 18px 6px}
  .quad--diversify{left:301px;top:240px;background:var(--sky);align-items:flex-start;padding:12px 14px 6px}
</style>
</head>
<body>

<section class="slide slide--cover">
  <div class="cover-bands">
    <span class="band-navy"></span><span class="band-blue"></span><span class="band-teal"></span><span class="band-orange"></span>
  </div>
  <h1 class="cover-title">This Your Presentation Title</h1>
  <p class="cover-presenter">Presenter</p>
  <p class="cover-date">01/09/2014</p>
  <p class="brand-name">Harrowby &amp; Co.</p>
  <p class="brand-tagline">Accounting, Taxation &amp; Strategic Business Advisors</p>
</section>

<section class="slide slide--method">
  <div class="side-bands"><span class="light"></span><span class="dark"></span></div>
  <div class="brand-mark" aria-label="Harrowby &amp; Co"><span class="dot"></span></div>
  <h2 class="slide-heading">Sample Heading</h2>
  <div class="heading-rule"></div>
  <h3 class="subheading">Now-Where-How</h3>
  <p class="body-copy">Now-Where-How is a simple but effective<br>process for problem solving and decision-<br>making. The first step is to understand your<br>current situation (Now), then assume you<br>are very successful and hence identify<br>your end-goals (Where), and only then<br>create strategies (How) to get from Now<br>to Where. A typical mistake many<br>organisations make is to discuss the<br>problem (Now) and then seek to solve it<br>immediately (How). Including the extra<br>step of Where means you have a<br>common view of the future and a means<br>to measure the potential effectiveness of<br>the strategies created.</p>
  <svg class="cycle" viewBox="0 0 576 432" aria-hidden="true">
    <defs>
      <marker id="arrowhead" markerWidth="6" markerHeight="6" refX="5" refY="3" orient="auto">
        <path d="M0,0 L6,3 L0,6 Z" fill="#9cc3e6"/>
      </marker>
    </defs>
    <g fill="none" stroke="#9cc3e6" stroke-width="1.2" marker-end="url(#arrowhead)">
      <path d="M386 139 L386 148"/>
      <path d="M452 185 Q474 192 466 225"/>
      <path d="M466 287 Q466 326 458 334"/>
      <path d="M312 340 Q292 330 298 288"/>
      <path d="M300 225 Q300 192 316 186"/>
    </g>
  </svg>
  <div class="cycle-box cycle-box--scan">SCAN – Research and data gathering including stakeholder input and other business and government scanning</div>
  <div class="cycle-box cycle-box--now">NOW – A summary of the current situation derived by analyzing the information gathered in the Scan, and identifying priority issues or strategic priorities</div>
  <div class="cycle-box cycle-box--how">HOW – Programs, projects and activities to achieve the end-points, including a way to measure success</div>
  <div class="cycle-box cycle-box--where">WHERE – End-points to successful period of time (e.g. four years), in terms of objectives, outcomes and impact</div>
  <div class="cycle-box cycle-box--next">Next Level of Planning</div>
  <p class="page-no">1</p>
</section>

<section class="slide slide--values">
  <div class="side-bands"><span class="light"></span><span class="dark"></span></div>
  <div class="brand-mark" aria-label="Harrowby &amp; Co"><span class="dot"></span></div>
  <h2 class="slide-heading">The value of the Entrepreneur</h2>
  <div class="heading-rule"></div>
  <ul class="value-list">
    <li>Find and work with a trusted business<br>advisor</li>
    <li>Understand and drive economic<br>value creation</li>
    <li>Measure and improve free cash flow</li>
    <li>Identify and improve the economic<br>denominator</li>
    <li>Sharpen and maintain focus</li>
    <li>Measure and improve processes</li>
    <li>Limit the number of strategic goals</li>
  </ul>
  <div class="value-divider"></div>
  <div class="quote-mark">“</div>
  <div class="quote-lines">
    <p>It’s about <em>innovation</em>…</p>
    <p>and managing <em>change</em>…</p>
    <p>and making decisions with<br><em>incomplete information</em>…</p>
    <p>and bearing <em>risk</em>…</p>
  </div>
  <p class="page-no">2</p>
</section>

<section class="slide slide--growth">
  <div class="side-bands"><span class="light"></span><span class="dark"></span></div>
  <div class="brand-mark" aria-label="Harrowby &amp; Co"><span class="dot"></span></div>
  <h2 class="slide-heading">Understanding business growth and diversification</h2>
  <div class="heading-rule"></div>
  <div class="matrix-line matrix-line--corner"></div>
  <p class="matrix-axis-label">Basis for Business Growth</p>
  <div class="matrix-line matrix-line--axis"></div>
  <div class="matrix-line matrix-line--top"></div>
  <p class="matrix-col" style="left:86px">Existing Customers</p>
  <p class="matrix-col" style="left:301px">New Customers</p>
  <p class="matrix-row" style="top:159px">Existing Products &amp;<br>Services</p>
  <p class="matrix-row" style="top:289px">New Products &amp;<br>Services</p>
  <div class="quad quad--existing">The easiest, lowest risk business growth often comes from focusing on more of your existing business</div>
  <div class="quad quad--customer">A medium risk strategy because only one variable, the customer, is being changed</div>
  <div class="quad quad--product">A medium risk strategy because only one variable, the product or service, is being changed</div>
  <div class="quad quad--diversify">Diversification is the highest risk approach to growth—because two variables are being changed at the one time</div>
  <p class="page-no">4</p>
</section>

</body>
</html>
```